Brightmere Business Card Redesign & Logo Update

We need to update our business cards to something more modern and fresh. Brightmere can provide the current color schemes and old design examples, but welcome creativity in helping us with this redesign. PLEASE NOTE that we no longer utilize the "tree" and/or "leaf" imagery in our branding. If able would apprecaite an update on the quality of our "words only" logo in Ai. / PNG formats too.

Target Market(s)

Investors, landowners, corporate partners, contractors

Industry/Entity Type

Environmental Restoration & Conservation

Contact Information for Business Card

Logo, persons name, title, mailing address, phone and email, website url

Font styles to use
Other font styles liked:
• Merriweather

Requirements
Nice to have
• Logo, persons name, title, mailing address, phone and email, website url, but open to ideams
Should not have
• No all back backgrounds

```html
<!DOCTYPE html>
<html lang="en">
<head>
<meta charset="utf-8">
<title>Brightmere Business Card</title>
<link href="https://fonts.googleapis.com/css2?family=Montserrat:wght@400;500;700&display=swap" rel="stylesheet">
<style>
  :root {
    --green: #177f43;
    --orange: #ee7f23;
    --white: #ffffff;
    --ink: #1d1d1d;
    --backdrop: #5b4632;
  }
  * { margin: 0; padding: 0; box-sizing: border-box; }
  html, body { width: 901px; height: 1200px; overflow: hidden; }
  body {
    background: var(--backdrop);
    font-family: "Montserrat", Arial, sans-serif;
    position: relative;
  }
  .card {
    position: absolute;
    left: 87px;
    width: 727px;
    border-radius: 22px;
    overflow: hidden;
    box-shadow: 0 6px 10px rgba(0,0,0,0.45);
  }
  .card-front { top: 143px; height: 422px; background: var(--white); }
  .card-back { top: 630px; height: 418px; background: var(--green); }
  .bands { position: absolute; inset: 0; width: 727px; height: 422px; }
  .bands .green { fill: var(--green); }
  .bands .orange { fill: var(--orange); }

  .person { position: absolute; left: 34px; top: 84px; }
  .person-name {
    font-weight: 700; font-size: 22px; letter-spacing: 0.2px;
    color: var(--orange); line-height: 1;
  }
  .person-name .first { color: var(--green); }
  .person-title { font-size: 17px; color: var(--ink); margin-top: 9px; }

  .wordmark {
    position: absolute; font-weight: 700; line-height: 1;
    letter-spacing: 0.5px;
  }
  .card-front .wordmark {
    right: 37px; top: 92px; font-size: 43px; color: var(--green);
  }
  .card-back .wordmark {
    left: 0; right: 0; text-align: center; top: 180px;
    font-size: 64px; color: var(--white);
  }

  .contacts { position: absolute; left: 34px; top: 263px; list-style: none; }
  .contacts li {
    display: flex; align-items: center; height: 34px;
    font-size: 20px; color: var(--ink);
  }
  .contacts .icon {
    width: 25px; height: 25px; margin-right: 13px; flex: none;
  }
  .contacts .icon circle { fill: var(--orange); }
  .contacts .icon .glyph { fill: none; stroke: var(--white); stroke-width: 1.6; stroke-linecap: round; stroke-linejoin: round; }

  .address {
    position: absolute; right: 37px; top: 306px; text-align: right;
    font-size: 19px; line-height: 26px; color: var(--ink); font-style: normal;
  }
</style>
</head>
<body>
  <section class="card card-front">
    <svg class="bands" viewBox="0 0 727 422" aria-hidden="true">
      <polygon class="green" points="0,0 727,0 727,24 261,24 239,46 0,46"/>
      <polygon class="orange" points="272,34 435,34 435,43 263,43"/>
      <rect class="green" x="440" y="34" width="125" height="9"/>
      <rect class="orange" x="571" y="34" width="156" height="9"/>
      <rect class="orange" x="0" y="377" width="153" height="10"/>
      <rect class="green" x="158" y="377" width="124" height="10"/>
      <polygon class="orange" points="288,377 470,377 461,387 288,387"/>
      <polygon class="green" points="486,375 727,375 727,422 0,422 0,396 463,396"/>
    </svg>

    <div class="person">
      <p class="person-name"><span class="first">DALE</span> HARTWELL</p>
      <p class="person-title">Managing Director</p>
    </div>

    <p class="wordmark">BRIGHTMERE</p>

    <ul class="contacts">
      <li>
        <svg class="icon" viewBox="0 0 25 25" aria-hidden="true">
          <circle cx="12.5" cy="12.5" r="12.5"/>
          <path class="glyph" d="M6 10c0-2 3-3 6.5-3s6.5 1 6.5 3v1h-3v-1.5h-7V11H6z M8.5 12h8l1.5 6H7z"/>
        </svg>
        555-214-7730
      </li>
      <li>
        <svg class="icon" viewBox="0 0 25 25" aria-hidden="true">
          <circle cx="12.5" cy="12.5" r="12.5"/>
          <path class="glyph" d="M6 8h13v9H6z M6 8l6.5 5L19 8 M6 17l5-4.5 M19 17l-5-4.5"/>
        </svg>
        info@brightmere.com
      </li>
      <li>
        <svg class="icon" viewBox="0 0 25 25" aria-hidden="true">
          <circle cx="12.5" cy="12.5" r="12.5"/>
          <path class="glyph" d="M12.5 5.5a7 7 0 1 0 0.01 0z M5.5 12.5h14 M12.5 5.5c-3 3.5-3 10.5 0 14 M12.5 5.5c3 3.5 3 10.5 0 14"/>
        </svg>
        www.brightmere.com
      </li>
    </ul>

    <address class="address">42-07 Linden Ave 14<br>Fairview, NY 11470</address>
  </section>

  <section class="card card-back">
    <p class="wordmark">BRIGHTMERE</p>
  </section>
</body>
</html>
```